Business Card Design for Boutique Agriculture Consulting Practice

Develop a modern Business card design using uploaded logos . Using the color specs 6C344F rgb(108, 52, 79) The fonts are trajan pro and eurostile. The business owner is a woman and should have a hint of femininity. This is what is behind the naming of the company: Rock roads are synonymous with the rural US landscape, where the corn grows and the cattle graze or for Fern Gully Advisory home. But don’t let the dust get in your eyes, rock roads have edge and are often the only path to a spectacular destination. To navigate them one must know where they are going, have the courage to take a new path and the willingness to adjust their plans to get there.
Target Market(s)
Marketing Professionals
Industry/Entity Type
Agriculture
Contact Information for Business Card
Maribeth Tolland
Title: Founder and CEO
Address: 20473 Wesley Lane, Olathe Kansas 66218
Email: mt@ferngullyadvisory.com
Phone: 317.554.2019
Website: www.ferngullyadvisory.com
Font styles to use
Other font styles liked:
- trajan pro and eurostile
Requirements
Must have
- Please use the correct color specs. Logo color specs are 6C344F rgb(108, 52, 79) The fonts are trajan pro and eurostile. Name, email and phone be the most important information included on the card
Should not have
- additional graphics

```html
<!DOCTYPE html>
<html lang="en">
<head>
<meta charset="utf-8">
<title>Fern Gully Advisory — Business Card</title>
<link rel="stylesheet" href="https://fonts.googleapis.com/css2?family=Cinzel:wght@400;600&family=Lato:wght@400&display=swap">
<style>
  :root {
    --stage: #2d0019;
    --plum: #6c344f;
    --plum-back: #6e3551;
    --plum-pattern: #7a4560;
    --card-white: #ffffff;
    --ink: #3b2b33;
    --rule: #a78596;
  }
  * { margin: 0; padding: 0; box-sizing: border-box; }
  html, body { width: 1200px; height: 900px; overflow: hidden; }
  body { background: var(--stage); position: relative; font-family: "Lato", Arial, sans-serif; }

  .card {
    position: absolute;
    top: 306px;
    width: 439px;
    height: 271px;
    border-radius: 10px;
    box-shadow: 0 3px 4px rgba(0,0,0,0.55);
    overflow: hidden;
  }
  .card--front { left: 149px; background: var(--card-white); }
  .card--back { left: 609px; background: var(--plum-back); }

  .brand-name {
    position: absolute;
    font-family: "Cinzel", "Times New Roman", serif;
    font-weight: 600;
    text-align: center;
    line-height: 1.15;
    letter-spacing: 0.5px;
  }
  .card--front .brand-name {
    left: 20px; width: 180px; top: 102px;
    font-size: 22px; color: var(--plum);
  }
  .card--back .brand-name {
    left: 280px; width: 120px; top: 120px;
    font-size: 14px; color: var(--card-white);
  }

  .divider {
    position: absolute; left: 213px; top: 73px;
    width: 1px; height: 124px; background: var(--rule);
  }

  .contact { position: absolute; left: 229px; top: 70px; color: var(--ink); }
  .contact__name {
    font-family: "Cinzel", "Times New Roman", serif;
    font-size: 17px; color: var(--plum); letter-spacing: 0.6px; line-height: 20px;
  }
  .contact__title { font-size: 12.5px; line-height: 16px; margin-bottom: 5px; }
  .contact__address { font-size: 12.5px; line-height: 16px; margin-bottom: 7px; }
  .contact__line { font-size: 12.5px; line-height: 16px; display: flex; align-items: center; gap: 4px; }
  .contact__line svg { width: 9px; height: 9px; fill: var(--ink); flex: none; }

  .back-pattern { position: absolute; inset: 0; background: var(--plum-back); }
</style>
</head>
<body>
  <section class="card card--front">
    <div class="brand-name">Fern Gully<br>Advisory</div>
    <div class="divider"></div>
    <div class="contact">
      <div class="contact__name">MARIBETH TOLLAND</div>
      <div class="contact__title">Founder and CEO</div>
      <div class="contact__address">20473 Wesley Lane<br>Olathe Kansas 66218</div>
      <div class="contact__line">
        <svg viewBox="0 0 10 10"><path d="M1 3.5 Q5 0.5 9 3.5 L8 5 L6.5 4 V3.3 H3.5 V4 L2 5 Z M2.5 5.5 H7.5 L8.5 9 H1.5 Z"/></svg>
        <span>317.554.2019</span>
      </div>
      <div class="contact__line">
        <svg viewBox="0 0 10 10"><path d="M0.5 2 H9.5 V8 H0.5 Z M0.5 2 L5 5.5 L9.5 2" stroke="#fff" stroke-width="0.8"/></svg>
        <span>mt@ferngullyadvisory.com</span>
      </div>
      <div class="contact__line">
        <svg viewBox="0 0 10 10"><circle cx="5" cy="5" r="4.5"/></svg>
        <span>www.ferngullyadvisory.com</span>
      </div>
    </div>
  </section>

  <section class="card card--back">
    <div class="back-pattern" role="img" aria-label="Faint repeating brand-mark pattern in light plum tones"></div>
    <div class="brand-name">Fern Gully<br>Advisory</div>
  </section>
</body>
</html>
```